It is a leisure sector investment company.The company plans to invest in a luxurious 5 star resort

We need a stationery design to our company 'Copper Lantern Limited' using the winning logo design. We need the letter heads, envelopes & the business cards. Should be simple, plain and professional
We have upload the source file & vector files which gives our logo design. We prefer the bottom logo.

Have updated under 'must have priorities', the company name, address, tel no. fax no. & the company reg no. which should come on the letter head. the long envelope should have the company name, tel & fax no. 
Business card should have the company name, name on the card, designation, tel no. fax no.  

- Letter head details:
Copper Lantern Limited
14 Floor, South Wing, Halvard Merchant Plaza,
Merrow Court, Colombo 01, Sri Lanka
Tel: +94 11 5047293 Fax: +94 11 5047298
Company Reg No.QX 6142
Long Envelope should have only the company name, adress, Tel & Fax
Business Cards should have the company name, Tel & Fax:
Business Card 1 - Lasantha Gunaratne - Chairman
Business Card 2 - Nimal.T.Wijesooriya - COO

```html
<!DOCTYPE html>
<html lang="en">
<head>
<meta charset="utf-8">
<title>Copper Lantern Limited – Stationery</title>
<link href="https://fonts.googleapis.com/css2?family=Arimo:wght@400&display=swap" rel="stylesheet">
<style>
  :root {
    --sheet: #ffffff;
    --frame: #8a8a8a;
    --outline: #3d3d3d;
    --brand: #4b4540;
    --umber: #4a4039;
    --umber-light: #584d45;
    --gold: #c9a05a;
    --caption: #222222;
  }
  * { margin: 0; padding: 0; box-sizing: border-box; }
  html, body { width: 1200px; height: 900px; overflow: hidden; background: var(--sheet); }
  .board {
    position: relative; width: 1200px; height: 900px;
    box-shadow: inset 1px 1px 0 var(--frame), inset 0 -1px 0 var(--frame);
    font-family: "Arimo", Arial, sans-serif;
  }
  .piece { position: absolute; }
  .card { width: 231px; height: 132px; }
  .card--front { border: 1px solid var(--outline); background: var(--sheet); }
  .card--back { overflow: hidden; }
  .texture {
    position: absolute; inset: 0;
    background: radial-gradient(ellipse at center, var(--umber-light), var(--umber) 75%);
  }
  .caption {
    position: absolute; width: 231px; text-align: center;
    font-size: 7px; color: var(--caption);
  }
  .company-name {
    position: absolute; left: 0; right: 0; text-align: center;
    font-family: "Arimo", Arial, sans-serif; font-weight: 400; color: var(--brand);
    line-height: 1; white-space: nowrap;
  }
  .card .company-name { top: 62px; font-size: 12px; }
  .card-text {
    position: absolute; left: 0; right: 0; text-align: center;
    color: var(--gold); font-size: 6.4px; line-height: 8.6px;
  }
  .card-text--name { top: 44px; }
  .card-text--address { top: 87px; }
  .letterhead { left: 483px; top: 60px; width: 544px; height: 757px; border: 1px solid var(--outline); background: var(--sheet); overflow: hidden; }
  .letterhead .company-name { top: 62px; font-size: 17px; }
  .letterhead__footer { position: absolute; left: 0; right: 0; bottom: 0; height: 34px; }
  .letterhead__footer .card-text { top: 7px; font-size: 7.6px; line-height: 10px; }
  .caption--letter { left: 483px; width: 544px; top: 833px; }
</style>
</head>
<body>
<main class="board">

  <section class="piece card card--front" style="left:176px; top:91px;">
    <p class="company-name">Copper Lantern Limited</p>
  </section>
  <p class="caption" style="left:176px; top:234px;">Visiting Card 1 Front</p>

  <section class="piece card card--back" style="left:176px; top:264px;">
    <div class="texture" role="img" aria-label="Dark umber ornamental damask pattern"></div>
    <p class="card-text card-text--name">Lasantha Gunaratne - Chairman</p>
    <p class="card-text card-text--address">Copper Lantern Limited<br>14 Floor, South Wing, Halvard Merchant Plaza,<br>Merrow Court, Colombo 01, Sri Lanka<br>Tel: +94 11 5047293, Fax: +94 11 5047298</p>
  </section>
  <p class="caption" style="left:176px; top:407px;">Visiting Card 1 Back</p>

  <section class="piece card card--front" style="left:176px; top:477px;">
    <p class="company-name">Copper Lantern Limited</p>
  </section>
  <p class="caption" style="left:176px; top:620px;">Visiting Card 2 Front</p>

  <section class="piece card card--back" style="left:176px; top:651px;">
    <div class="texture" role="img" aria-label="Dark umber ornamental damask pattern"></div>
    <p class="card-text card-text--name">Nimal.T.Wijesooriya - COO</p>
    <p class="card-text card-text--address">Copper Lantern Limited<br>14 Floor, South Wing, Halvard Merchant Plaza,<br>Merrow Court, Colombo 01, Sri Lanka<br>Tel: +94 11 5047293, Fax: +94 11 5047298</p>
  </section>
  <p class="caption" style="left:176px; top:794px;">Visiting Card 2 Back</p>

  <section class="piece letterhead">
    <p class="company-name">Copper Lantern Limited</p>
    <footer class="letterhead__footer">
      <div class="texture" role="img" aria-label="Dark umber ornamental damask pattern"></div>
      <p class="card-text">Copper Lantern Limited, 14 Floor, South Wing, Halvard Merchant Plaza, Merrow Court, Colombo 01, Sri Lanka<br>Tel: +94 11 5047293, Fax: +94 11 5047298, Company Reg No.QX 6142</p>
    </footer>
  </section>
  <p class="caption caption--letter">Letter Head</p>

</main>
</body>
</html>
```